Consultancy Business Card Design

We need a business card design for a new company based in singapore called FortyOne. FortyOne a boutique consultancy firm offering broad-based business solutions, from conception to re-invention, for ventures from new start-ups to long-running traditional businesses.
Its 2 main divisions (Food & Beverage Operations and Construction & Project Management) have access to a wide range of networks, knowledge bases, and resources to service its clients across numerous diverse sectors. This includes, and is not limited to, construction, F&B, and retail.
We are a company that combines the ambition, boldness and energy of one in the 20s with the dedication, level-headedness and dependability of one entering its 30s. Bridging the experiences of the old with ideals of the young, we draw on the positives of both to create a unique synergy.
We hope to see designs that fits our company profile.
Boutique
Contact Information for Business Card
FortyOne(Company Name)
Marcus Tan (Name)
Principle Consultant (Title)
F&B and Hospitality (Division)
(+65) 8364 5107 (Contact no.)
marcus@fortyone-example.com.sg (Email)
Colors
Designer to choose colors to be used in the design.

```html
<!DOCTYPE html>
<html lang="en">
<head>
<meta charset="UTF-8">
<title>FortyOne Business Card</title>
<link href="https://fonts.googleapis.com/css2?family=Source+Sans+3:wght@400;600&display=swap" rel="stylesheet">
<style>
  :root {
    --stage: #2b2b2d;
    --ink: #111111;
    --black-top: #1c1c1e;
    --black-bottom: #050505;
    --paper: #ffffff;
    --paper-shade: #ececec;
    --accent: #d3202e;
    --muted: #6e6e6e;
    --light: #f2f2f2;
  }
  * { margin: 0; padding: 0; box-sizing: border-box; }
  html, body { width: 1200px; height: 849px; overflow: hidden; }
  body {
    background: var(--stage);
    font-family: "Source Sans 3", sans-serif;
    display: flex;
    flex-direction: column;
    align-items: center;
    justify-content: center;
    gap: 40px;
  }
  .card {
    width: 640px;
    height: 366px;
    border-radius: 26px;
    position: relative;
    overflow: hidden;
    box-shadow: 0 12px 30px rgba(0,0,0,0.45);
  }

  .company-name {
    font-weight: 400;
    line-height: 1;
    white-space: nowrap;
  }

  /* Back side */
  .card-back {
    background: linear-gradient(160deg, var(--black-top) 0%, var(--black-bottom) 70%);
    display: flex;
    align-items: center;
    justify-content: center;
  }
  .card-back .company-name { color: var(--muted); font-size: 72px; }

  /* Front side */
  .card-front { background: var(--paper); }
  .front-header {
    position: absolute;
    top: 0; left: 0; right: 0;
    height: 218px;
    background: linear-gradient(180deg, var(--paper) 0%, var(--paper-shade) 100%);
    display: flex;
    align-items: center;
    justify-content: center;
  }
  .front-header .company-name { color: var(--ink); font-size: 64px; }

  .accent-rule {
    position: absolute;
    top: 218px; left: 0; right: 0;
    height: 5px;
    background: var(--accent);
  }
  .contact-band {
    position: absolute;
    top: 223px; left: 0; right: 0; bottom: 0;
    background: linear-gradient(180deg, var(--black-top), var(--black-bottom));
    display: flex;
    align-items: center;
    padding: 0 40px;
    color: var(--light);
  }
  .person { text-align: right; width: 190px; flex: none; }
  .person-name { font-size: 25px; font-weight: 400; white-space: nowrap; }
  .person-title, .person-division { font-size: 16px; line-height: 1.3; white-space: nowrap; }
  .band-divider {
    width: 3px;
    height: 86px;
    background: var(--accent);
    margin: 0 22px;
    flex: none;
  }
  .contact-list { list-style: none; }
  .contact-item {
    display: flex;
    align-items: center;
    gap: 10px;
    font-size: 19px;
    line-height: 1.45;
    white-space: nowrap;
  }
  .contact-icon { width: 18px; height: 18px; flex: none; }
</style>
</head>
<body>

  <section class="card card-back">
    <div class="company-name">FortyOne</div>
  </section>

  <section class="card card-front">
    <div class="front-header">
      <div class="company-name">FortyOne</div>
    </div>
    <div class="accent-rule"></div>
    <div class="contact-band">
      <div class="person">
        <div class="person-name">Marcus Tan</div>
        <div class="person-title">Principle Consultant</div>
        <div class="person-division">F&amp;B and Hospitality</div>
      </div>
      <div class="band-divider"></div>
      <ul class="contact-list">
        <li class="contact-item">
          <svg class="contact-icon" viewBox="0 0 20 20" aria-hidden="true">
            <circle cx="10" cy="10" r="10" fill="#d3202e"/>
            <path d="M7 5.5c.6-.4 1.2 0 1.5.6l.6 1.3c.2.5 0 1-.4 1.3l-.5.3c.4 1 1.3 1.9 2.3 2.3l.3-.5c.3-.4.8-.6 1.3-.4l1.3.6c.6.3 1 .9.6 1.5-.6 1-1.8 1.3-2.9.8A8 8 0 0 1 6.2 8.4C5.7 7.3 6 6.1 7 5.5z" fill="#fff"/>
          </svg>
          <span>(+65) 8364 5107</span>
        </li>
        <li class="contact-item">
          <svg class="contact-icon" viewBox="0 0 20 20" aria-hidden="true">
            <circle cx="10" cy="10" r="10" fill="#d3202e"/>
            <rect x="5" y="6.5" width="10" height="7" rx="1" fill="#fff"/>
            <path d="M5.5 7l4.5 3.5L14.5 7" stroke="#d3202e" stroke-width="1.2" fill="none"/>
          </svg>
          <span>marcus@fortyone-example.com.sg</span>
        </li>
        <li class="contact-item">
          <svg class="contact-icon" viewBox="0 0 20 20" aria-hidden="true">
            <circle cx="10" cy="10" r="10" fill="#d3202e"/>
            <circle cx="10" cy="10" r="5" stroke="#fff" stroke-width="1.3" fill="none"/>
            <path d="M5 10h10M10 5c-2.2 2.8-2.2 7.2 0 10M10 5c2.2 2.8 2.2 7.2 0 10" stroke="#fff" stroke-width="1.1" fill="none"/>
          </svg>
          <span>www.fortyone-example.com.sg</span>
        </li>
      </ul>
    </div>
  </section>

</body>
</html>
```